Business Card Design

Brantock Energy, L.P. is an energy and lifecycle management firm that creates value in petroleum products through synergistic marketing, trading, recovery, logistics and beneficial reuse services.

Sell top-quality refinery feedstock, petroleum products and co-products on the spot and futures makets (energy trading)

Separate, reclaim and/or manufacture valuable products for beneficial reuse (environmental)
Updates

The tag line Understanding Solutions   Performance are three different concepts and need to be kept either spaced apart or separated in some way. Thanks. 

Target Market(s)

Refiners, Petroleum storage companies, energy marketers

Industry/Entity Type

Business

Contact Information for Business Card

Glenda M. Holloway
Principal
Brantock Energy, L.P.
4817 Quimby St.
Houston, TX 77310
713-482-6159 phone
713-624-8841 fax
g.holloway@brantockenergy-example.com
www.brantockenergy-example.com

Requirements
Must have
• Tagline outlined in matching orange -

Understanding Solutions Performance
Nice to have
• Coordinating typestyles

```html
<!DOCTYPE html>
<html lang="en">
<head>
<meta charset="utf-8">
<title>Brantock Energy, L.P. — Business Card</title>
<link rel="stylesheet" href="https://fonts.googleapis.com/css2?family=Michroma&family=Orbitron:wght@500;700&display=swap">
<style>
  :root {
    --ink: #1e1e1e;
    --band: #1b1b1b;
    --orange: #f15a22;
    --paper: #ffffff;
    --backdrop: #e9e9e7;
  }
  * { margin: 0; padding: 0; box-sizing: border-box; }
  html, body { width: 1200px; height: 1000px; overflow: hidden; }
  body {
    background: var(--backdrop);
    position: relative;
    font-family: "Michroma", "Orbitron", sans-serif;
    color: var(--ink);
  }
  .card {
    position: absolute;
    left: 100px; top: 214px;
    width: 1000px; height: 572px;
    background: var(--paper);
    border-radius: 40px;
    overflow: hidden;
    box-shadow: 0 10px 30px rgba(0,0,0,.15);
  }
  .card__band {
    position: absolute; left: 0; top: 0;
    width: 62px; height: 100%;
    background: var(--band);
  }
  .brand {
    position: absolute; left: 300px; top: 70px;
    display: flex; align-items: center; gap: 22px;
  }
  .brand__dot {
    width: 90px; height: 90px; border-radius: 50%;
    background: var(--ink);
    flex: none;
  }
  .brand__name {
    font-family: "Orbitron", sans-serif;
    font-weight: 700;
    font-size: 40px;
    line-height: 1.05;
    letter-spacing: 2px;
    text-transform: uppercase;
    color: var(--ink);
  }
  .tagline {
    position: absolute; left: 150px; top: 196px;
    width: 740px;
    display: flex; justify-content: space-between;
    font-family: "Orbitron", sans-serif;
    font-weight: 700;
    font-size: 21px;
    letter-spacing: 2px;
    text-transform: uppercase;
    color: var(--orange);
  }
  .person {
    position: absolute; left: 100px; top: 258px;
    width: 900px;
    text-transform: uppercase;
  }
  .person__name { font-size: 20px; letter-spacing: 1.5px; }
  .person__role {
    display: flex; align-items: flex-end; gap: 10px;
    margin-top: 4px;
  }
  .person__title { font-size: 17px; letter-spacing: 1px; line-height: 1.2; flex: none; }
  .person__rule {
    flex: 1;
    height: 8px;
    margin-bottom: 3px;
    background: var(--orange);
  }
  .icons {
    position: absolute; left: 18px; top: 338px;
    display: flex; flex-direction: column; gap: 10px;
  }
  .icons svg { display: block; width: 26px; height: 26px; }
  .contact {
    position: absolute; left: 96px; top: 340px;
    list-style: none;
    font-size: 13px;
    letter-spacing: .5px;
    line-height: 36px;
    text-transform: uppercase;
  }
  .address {
    position: absolute; left: 630px; top: 392px;
    font-style: normal;
    text-transform: uppercase;
    line-height: 38px;
  }
  .address__company { font-size: 14px; letter-spacing: 4px; }
  .address__street { font-size: 14px; letter-spacing: 1px; }
</style>
</head>
<body>
  <section class="card" aria-label="Business card">
    <div class="card__band"></div>

    <div class="brand">
      <span class="brand__dot"></span>
      <span class="brand__name">Brantock Energy,<br>L.P.</span>
    </div>

    <p class="tagline"><span>Understanding</span><span>Solutions</span><span>Performance</span></p>

    <div class="person">
      <p class="person__name">Glenda M. Holloway</p>
      <div class="person__role">
        <p class="person__title">Principal</p>
        <span class="person__rule"></span>
      </div>
    </div>

    <div class="icons" aria-hidden="true">
      <svg viewBox="0 0 26 26"><rect width="26" height="26" fill="var(--orange)"/><path d="M8 6c-1 1-1.5 3 1 7s5 6 7 6c1 0 2-.5 2.5-1.5l-3-2.5-1.5 1.2c-1.5-.6-3.6-2.8-4.2-4.2l1.2-1.5L8.5 5.8z" fill="#fff"/></svg>
      <svg viewBox="0 0 26 26"><rect width="26" height="26" fill="var(--orange)"/><rect x="8" y="5" width="10" height="6" fill="#fff"/><rect x="5" y="11" width="16" height="8" fill="#fff"/><rect x="8" y="16" width="10" height="5" fill="var(--orange)" stroke="#fff" stroke-width="1.5"/></svg>
      <svg viewBox="0 0 26 26"><rect width="26" height="26" fill="var(--orange)"/><rect x="5" y="8" width="16" height="11" fill="#fff"/><path d="M5 8l8 6 8-6" fill="none" stroke="var(--orange)" stroke-width="1.5"/></svg>
      <svg viewBox="0 0 26 26"><rect width="26" height="26" fill="var(--orange)"/><circle cx="13" cy="13" r="7.5" fill="none" stroke="#fff" stroke-width="1.5"/><ellipse cx="13" cy="13" rx="3.2" ry="7.5" fill="none" stroke="#fff" stroke-width="1.5"/><path d="M5.5 13h15" stroke="#fff" stroke-width="1.5"/></svg>
    </div>

    <ul class="contact">
      <li>77310 713-482-6159</li>
      <li>713-624-8841</li>
      <li>g.holloway@brantockenergy-example.com</li>
      <li>www.brantockenergy-example.com</li>
    </ul>

    <address class="address">
      <p class="address__company">Brantock Energy, L.P.</p>
      <p class="address__street">4817 Quimby St. Houston, TX</p>
    </address>
  </section>
</body>
</html>
```